VelmoRay.com 11x17 folded Horticulture products -coco peat /greenhouse Growers/big box resellers

2 similar Contemporary design with mini catalog page inside facing page of one catalog, with some bold photos for cover and some call outs inside. I have attached a mock-up of the first brochure I did, and I need everything set up in In Design so I can modify it as needed. Both must be done in InDesign and set up for professional printing. If it cannot be created in In Design, please do not submit a design. I will work on the copy for the inside copy of brochure #2 once I have blocking.

Target Market(s)

Large Commercial growers around the world and resellers to home gardening stores.
Coco peat is made from

Font styles to use
Sans Serif

Colors
0255a3
9bcb3b
6b449b

Requirements
Must have
• Color/white contrast, no background leafy stuff that looks like clip art from Quorbel Press
• Colors must match the CMYK tones in the logo (there are many, but especially a distinctive blue and a distinctive dark green that will work for lettering and boxed text
• Logo doesn't have a dark purple or tan (like coco peat) but a third color would be helpful
Nice to have
• areas inside rt facing page or across the bottom of the two facing pages where I can list little 2x2" or 2x3" blurbs about products or services, and space on the back cover to feature a 150-200 word "about us" story.
Should not have
• No light lime green or yellow, and if there is a gradient used, it should have a function.
• No shadow effects on fonts.
• The name of the company is Velmoray.com and the logo is available on their website

```html
<!DOCTYPE html>
<html lang="en">
<head>
<meta charset="utf-8">
<title>VelmoRay brochure spread</title>
<link rel="stylesheet" href="https://fonts.googleapis.com/css2?family=Lato:ital,wght@0,400;0,700;0,900;1,700&display=swap">
<style>
  :root {
    --velmo-blue: #0255a3;
    --velmo-green: #9bcb3b;
    --velmo-teal: #3e8f96;
    --headline-grey: #454545;
    --body-grey: #3a3a3a;
    --paper: #ffffff;
    --backdrop: #d9d9d9;
  }
  * { box-sizing: border-box; margin: 0; padding: 0; }
  html, body { width: 1200px; height: 840px; overflow: hidden; }
  body {
    background: var(--backdrop);
    font-family: "Lato", Arial, sans-serif;
    color: var(--body-grey);
    position: relative;
  }
  .spread {
    position: absolute;
    left: 40px; top: 58px;
    width: 1120px; height: 724px;
    display: flex;
  }
  .page {
    position: relative;
    width: 560px; height: 724px;
    background: var(--paper);
    overflow: hidden;
  }
  .page--back { border-right: 1px solid #e6e6e6; }

  /* shared bottom band: blue on the back flowing to green on the cover */
  .web-band {
    position: absolute; left: 0; bottom: 0;
    width: 100%; height: 74px;
    display: flex; align-items: center;
    color: #fff; font-size: 15px; letter-spacing: 2.5px; font-weight: 700;
  }
  .page--back .web-band {
    background: linear-gradient(90deg, var(--velmo-blue) 0%, #1c62a0 55%, var(--velmo-teal) 100%);
    padding-left: 70px;
  }
  .page--cover .web-band {
    background: linear-gradient(90deg, var(--velmo-teal) 0%, #6db462 50%, var(--velmo-green) 100%);
    justify-content: center;
  }

  /* back page */
  .services-title {
    position: absolute; left: 70px; top: 36px;
    color: var(--velmo-blue); font-size: 22px; font-weight: 400;
  }
  .services-box {
    position: absolute; left: 60px; top: 70px;
    width: 440px;
    border: 1.5px solid var(--velmo-blue);
    padding: 12px 16px;
    font-size: 9.5px; line-height: 1.45; text-align: justify;
  }
  .services-box p + p { margin-top: 10px; }

  .brand-mark {
    display: flex; align-items: center; gap: 8px;
    color: var(--velmo-blue); font-weight: 700;
  }
  .brand-mark__dot {
    border-radius: 50%; background: var(--velmo-green);
  }
  .page--back .brand-mark { position: absolute; left: 72px; top: 318px; font-size: 24px; }
  .page--back .brand-mark__dot { width: 22px; height: 22px; }

  .retail-info { position: absolute; left: 60px; top: 392px; width: 450px; }
  .retail-info__heading {
    color: var(--velmo-blue); font-size: 10.5px; font-weight: 700; font-style: italic;
    text-transform: uppercase; margin-bottom: 10px;
  }
  .retail-info__list { list-style: none; font-size: 10px; line-height: 1.4; }
  .retail-info__list li { position: relative; padding-left: 18px; margin-bottom: 8px; }
  .retail-info__list li::before {
    content: ""; position: absolute; left: 2px; top: 4px;
    width: 6px; height: 6px; border-radius: 50%; background: var(--velmo-blue);
  }
  .contact-list { list-style: none; margin-top: 6px; font-size: 10px; }
  .contact-list li { display: flex; align-items: center; gap: 10px; margin-bottom: 10px; }
  .contact-list svg { width: 14px; height: 14px; flex: none; }

  /* cover page */
  .cover-headline {
    position: absolute; right: 40px; top: 140px;
    text-align: right; color: var(--headline-grey);
    text-transform: uppercase; line-height: 1.05;
  }
  .cover-headline__small { display: block; font-size: 19px; font-weight: 700; letter-spacing: 1px; }
  .cover-headline__large { display: block; font-size: 40px; font-weight: 900; margin-bottom: 6px; }

  .cover-photo {
    position: absolute; left: 0; bottom: 74px;
    width: 100%; height: 300px;
    background:
      linear-gradient(180deg, rgba(255,255,255,1) 0%, rgba(255,255,255,0) 35%),
      linear-gradient(180deg, #e9eeea 0%, #c9d6cf 40%, #8fbf5a 72%, #4f8f34 100%);
  }
  .page--cover .brand-mark {
    position: absolute; left: 50%; top: 360px; transform: translateX(-50%);
    font-size: 34px;
  }
  .page--cover .brand-mark__dot { width: 30px; height: 30px; }
</style>
</head>
<body>
  <main class="spread">
    <section class="page page--back">
      <h2 class="services-title">Services</h2>
      <div class="services-box">
        <p>Lorem ipsum dolor sit amet, quis sem sit odio metus lorem, massa congue mattis dolor a turpis. Officia potenti. Volutpat maecenas posuere a maecenas dolor cras. Eget tristique neque quam rutrum suspendisse amet vivamus libero, quam et rhoncus tempus eu, proin sed nulla molestiae, interdum congue. Facilisi vel placerat purus rutrum aliquam augue, parturient pede tincidunt torquent.</p>
        <p>Augue sodales maecenas et. Eget auctor sit vitae neque nascetur, mollis nostra faucibus pariatur magnis lorem. Est rutrum sociis sit ultricies scelerisque. Blandit nec ullamcorper quis vitae, qui commodo vivamus bibendum aliquet vivamus. Et mauris in penatibus, amet cursus, vestibulum eros quis non orci ridiculus, gravida nunc in elementum.</p>
      </div>

      <div class="brand-mark"><span class="brand-mark__dot"></span>VelmoRay</div>

      <div class="retail-info">
        <h3 class="retail-info__heading">VelmoRay products are customizable for retail distribution:</h3>
        <ul class="retail-info__list">
          <li>Consumers who wants to create a cost-efficient container gar-den with simple 3-step Verdanta grow bags or quality Coco peat blocks and nutrients.</li>
          <li>Catalogue, on-line and store-front resellers of hydroponic and home garden supplies will have an affordable container gardening system that requires no tools or special expertise.</li>
        </ul>
        <ul class="contact-list">
          <li>
            <svg viewBox="0 0 24 24" aria-hidden="true"><path fill="#0255a3" d="M12 2a7 7 0 0 0-7 7c0 5 7 13 7 13s7-8 7-13a7 7 0 0 0-7-7zm0 9.5A2.5 2.5 0 1 1 12 6.5a2.5 2.5 0 0 1 0 5z"/></svg>
            Contact our Managing Director, Daniel Orrick, PhD.
          </li>
          <li>
            <svg viewBox="0 0 24 24" aria-hidden="true"><circle cx="12" cy="12" r="10" fill="none" stroke="#0255a3" stroke-width="2"/><path fill="#0255a3" d="M9 7l2 2-1.2 1.6a7 7 0 0 0 3.6 3.6L15 13l2 2-1.5 2C11 17 7 13 7 8.5z"/></svg>
            +1-555-014-2290
          </li>
          <li>
            <svg viewBox="0 0 24 24" aria-hidden="true"><rect x="2" y="5" width="20" height="14" rx="1" fill="#0255a3"/><path d="M2 6l10 7 10-7" fill="none" stroke="#fff" stroke-width="1.6"/></svg>
            info@velmoray.com
          </li>
        </ul>
      </div>

      <div class="web-band">www.velmoray.com</div>
    </section>

    <section class="page page--cover">
      <h1 class="cover-headline">
        <span class="cover-headline__small">Precision-designed</span>
        <span class="cover-headline__large">Coco coir mixes</span>
        <span class="cover-headline__small">Transforming</span>
        <span class="cover-headline__large">The growing world</span>
      </h1>

      <div class="cover-photo" role="img" aria-label="Photo of a greenhouse interior with long rows of young green lettuce plants under a white arched roof"></div>

      <div class="brand-mark"><span class="brand-mark__dot"></span>VelmoRay</div>

      <div class="web-band">www.velmoray.com</div>
    </section>
  </main>
</body>
</html>
```